We're a SEA Media Company that needs a fresh new look for one of our SG sites.

the site targets those that are researching apartment or home renovations and who want to get ideas and inspiration. the site is supported by a significant print magazine that is bi monthly. the attached design needs less grid and clutter.

the audience generally want to see designers and products they can use.

currently the site is zintaremura.com.sg.

```html
<!DOCTYPE html>
<html lang="en">
<head>
<meta charset="utf-8">
<title>zintaremura.com.sg — Home Renovations</title>
<link href="https://fonts.googleapis.com/css2?family=Titillium+Web:wght@300;400;600;700&display=swap" rel="stylesheet">
<style>
:root{
  --brand:#1aa3dc;
  --brand-dark:#1590c6;
  --ink:#1e1e1e;
  --text:#444;
  --muted:#777;
  --band-top:#f7f7f7;
  --band-bottom:#e2e2e2;
  --white:#fff;
}
*{box-sizing:border-box;margin:0;padding:0}
html,body{width:1200px;height:2375px;overflow:hidden}
body{position:relative;background:var(--white);font-family:"Titillium Web",Arial,sans-serif;color:var(--text)}
.abs{position:absolute}

/* header */
.site-header{left:0;top:0;width:1200px;height:119px;background:#fafafa;box-shadow:0 2px 6px rgba(0,0,0,.12);z-index:2}
.brand{left:106px;top:24px;font-size:44px;font-weight:400;color:var(--brand);letter-spacing:-.5px;white-space:nowrap}
.main-nav{left:575px;top:52px;display:flex}
.main-nav a{font-size:18px;color:#555;text-decoration:none;margin-right:31px}
.main-nav a:last-child{margin-right:0}

/* hero */
.hero{left:0;top:119px;width:1200px;height:415px;background:linear-gradient(100deg,#d9d0c2 0%,#f1ece4 35%,#cfc2ad 60%,#ece6dc 80%,#bfb39f 100%)}
.hero-label{left:108px;top:247px;width:473px;height:84px;background:var(--brand);color:var(--white);font-size:40px;font-weight:600;letter-spacing:2px;line-height:84px;text-align:center}
.hero-arrow{top:268px;width:40px;height:40px;border-radius:50%;background:var(--white);box-shadow:0 1px 3px rgba(0,0,0,.3)}
.hero-arrow svg{display:block}

/* band */
.intro-band{left:0;top:534px;width:1200px;height:120px;background:linear-gradient(var(--band-top),var(--band-bottom))}
.intro-text{left:106px;top:574px;width:800px;font-size:25px;color:#555;font-weight:400;white-space:nowrap}
.btn{background:var(--brand);color:var(--white);text-align:center;font-weight:400}
.contact-btn{left:928px;top:560px;width:161px;height:62px;line-height:62px;font-size:26px}

/* designers */
.section-title{font-weight:700;color:var(--ink);letter-spacing:3px}
.designers-title{left:0;top:680px;width:1200px;text-align:center;font-size:44px}
.designers-lead{left:175px;top:750px;width:850px;text-align:center;font-size:19px;line-height:33px;color:#444}
.designer-card{top:883px;width:230px;height:201px}
.card-1{left:106px;background:linear-gradient(135deg,#4bb8e2,#37a9db)}
.card-2{left:356px;background:linear-gradient(180deg,#f0f0f0,#d8d8d8)}
.card-3{left:606px;background:linear-gradient(180deg,#e8e8e8,#b9b9b9)}
.card-4{left:857px;background:linear-gradient(90deg,#c8dc3a 0%,#e6e6e6 30%,#bfbfbf 100%)}
.card-name{left:32px;top:40px;font-size:22px;font-weight:700;color:var(--white);line-height:24px;white-space:nowrap}
.card-group{left:32px;top:98px;font-size:17px;color:var(--white)}
.card-dot{top:146px;width:34px;height:34px;border:1.5px solid rgba(255,255,255,.85);border-radius:50%}
.pager{left:542px;top:1131px;display:flex;gap:7px}
.pager span{width:12px;height:12px;border:1.5px solid #888;border-radius:50%}
.pager span.on{background:#666;border-color:#666}

/* products */
.products-photo{left:108px;top:1195px;width:541px;height:360px;background:linear-gradient(160deg,#eaf4f8 0%,#cfe4ec 55%,#8fb394 100%)}
.products-title{left:673px;top:1176px;font-size:44px}
.products-text{left:673px;top:1256px;width:430px;font-size:18px;line-height:25px;color:#444}
.product-list{left:671px;top:1385px;list-style:none}
.product-list li{height:46px;display:flex;align-items:center;font-size:19px;color:#444}
.product-list svg{margin-right:16px}
.products-btn{left:671px;top:1564px;width:219px;height:57px;line-height:57px;font-size:20px}

/* magazine */
.mag-title{left:106px;top:1693px;font-size:22px;letter-spacing:1px}
.mag-all{left:985px;top:1696px;width:104px;text-align:right;font-size:17px;color:var(--muted);letter-spacing:1px}
.mag-row{left:106px;top:1741px;display:flex;gap:2px}
.mag-cover{width:195px;height:197px}
.cover-1{background:linear-gradient(135deg,#f2e48a,#7fa5b6)}
.cover-2{background:linear-gradient(160deg,#f4f0ea,#c0584a)}
.cover-3{background:linear-gradient(160deg,#3c4a52,#141414)}
.cover-4{background:linear-gradient(160deg,#e6e3dd,#8a9aa0)}
.cover-5{background:linear-gradient(160deg,#f4f4f2,#e2503c)}

/* footer */
.site-footer{left:0;top:1980px;width:1200px;height:297px;background:var(--brand)}
.foot-title{top:2026px;font-size:20px;font-weight:400;color:var(--white);white-space:nowrap}
.foot-text{font-size:13.5px;color:#d8f0fb;line-height:19px}
.social{left:106px;top:2209px;display:flex;gap:4px}
.social span{width:36px;height:36px;border-radius:50%;background:var(--white)}
.recent{left:440px;display:flex}
.recent-thumb{width:72px;height:60px;border:2px solid #7fd0f0;margin-right:12px}
.recent-title{font-size:14.5px;font-weight:600;color:var(--white);line-height:21px;width:220px}
.recent-date{font-size:12px;color:var(--white);margin-top:3px}
.mail-field{left:774px;top:2066px;width:205px;height:40px;background:var(--white);border:1px solid #9ad6ef;font-size:14px;color:#555;line-height:38px;padding-left:14px}
.subscribe-btn{left:774px;top:2129px;width:124px;height:41px;line-height:41px;font-size:15px;background:var(--brand-dark)}
.copyright{left:0;top:2277px;width:1200px;height:98px;background:var(--brand-dark);text-align:center;line-height:98px;font-size:13px;color:var(--white)}
</style>
</head>
<body>

<header class="abs site-header">
  <div class="abs brand">zintaremura.com.sg</div>
  <nav class="abs main-nav">
    <a href="#">Designers</a><a href="#">Projects</a><a href="#">Products</a><a href="#">Directory</a><a href="#">News</a><a href="#">Events</a>
  </nav>
</header>

<section class="abs hero" role="img" aria-label="Bright renovated apartment kitchen with white cabinetry and bar stools"></section>
<div class="abs hero-label">HOME RENOVATIONS</div>
<div class="abs hero-arrow" style="left:27px">
  <svg width="40" height="40" viewBox="0 0 40 40"><path d="M21 15l-5 5 5 5M26 15l-5 5 5 5" fill="none" stroke="#666" stroke-width="1.6"/></svg>
</div>
<div class="abs hero-arrow" style="left:1127px">
  <svg width="40" height="40" viewBox="0 0 40 40"><path d="M14 15l5 5-5 5M19 15l5 5-5 5" fill="none" stroke="#666" stroke-width="1.6"/></svg>
</div>

<div class="abs intro-band"></div>
<p class="abs intro-text">Researching apartment or home renovations and who want to get ideas...!</p>
<div class="abs btn contact-btn">Contact us</div>

<h2 class="abs section-title designers-title">OUR DESIGNERS</h2>
<p class="abs designers-lead">The team behind Calder Loft is made up of experienced designers with a diverse talent pool. Being a relatively young outfit mean...</p>

<div class="abs designer-card card-1" role="img" aria-label="Design team portrait behind a blue overlay">
  <div class="abs card-name">NORVANE STUDIO<br>PTE LTD</div>
  <div class="abs card-group">Teval Group</div>
  <span class="abs card-dot" style="left:32px"></span>
  <span class="abs card-dot" style="left:86px"></span>
</div>
<div class="abs designer-card card-2" role="img" aria-label="Three designers in white shirts"></div>
<div class="abs designer-card card-3" role="img" aria-label="Four designers seated in dark shirts"></div>
<div class="abs designer-card card-4" role="img" aria-label="Two designers in black outfits"></div>
<div class="abs pager"><span></span><span></span><span class="on"></span><span></span><span></span><span></span></div>

<div class="abs products-photo" role="img" aria-label="White bathroom with twin freestanding tubs and greenery"></div>
<h2 class="abs section-title products-title">OUR PRODUCTS</h2>
<p class="abs products-text">Lorem ipsum dolor sit amet, consectetuer adipiscing elit. Donec odio. Quisque volutpat mattis eros. Nullam malesuada erat ut turpis. Suspendisse urna nibh, viverra non, semper suscipit, posuere a, pede.</p>
<ul class="abs product-list">
  <li><svg width="22" height="22" viewBox="0 0 22 22"><circle cx="11" cy="11" r="11" fill="#cfcfcf"/><path d="M6 11l3.5 3.5L16 8" fill="none" stroke="#fff" stroke-width="2"/></svg>Finishes</li>
  <li><svg width="22" height="22" viewBox="0 0 22 22"><circle cx="11" cy="11" r="11" fill="#cfcfcf"/><path d="M6 11l3.5 3.5L16 8" fill="none" stroke="#fff" stroke-width="2"/></svg>Fittings</li>
  <li><svg width="22" height="22" viewBox="0 0 22 22"><circle cx="11" cy="11" r="11" fill="#cfcfcf"/><path d="M6 11l3.5 3.5L16 8" fill="none" stroke="#fff" stroke-width="2"/></svg>Furniture</li>
</ul>
<div class="abs btn products-btn">View More Products</div>

<h3 class="abs section-title mag-title">OUR MAGAZINE</h3>
<div class="abs mag-all">VIEW ALL</div>
<div class="abs mag-row">
  <div class="mag-cover cover-1" role="img" aria-label="Magazine cover with a bright study room"></div>
  <div class="mag-cover cover-2" role="img" aria-label="Magazine cover with a patterned sofa"></div>
  <div class="mag-cover cover-3" role="img" aria-label="Magazine cover with a designer portrait"></div>
  <div class="mag-cover cover-4" role="img" aria-label="Magazine cover with a living room and grey sofa"></div>
  <div class="mag-cover cover-5" role="img" aria-label="Magazine cover with colourful homeware buys"></div>
</div>

<footer class="abs site-footer"></footer>
<h4 class="abs foot-title" style="left:108px">Contact Info</h4>
<p class="abs foot-text" style="left:106px;top:2070px;width:260px">Lorem ipsum dolor sit amet, consectetur adipisicing elit, sed do eiusmod tempor</p>
<p class="abs foot-text" style="left:106px;top:2129px">(123) 5550 246810</p>
<p class="abs foot-text" style="left:106px;top:2160px">hello@vereluxhomes.sg</p>
<div class="abs social"><span></span><span></span><span></span><span></span></div>

<h4 class="abs foot-title" style="left:441px">Recent Project</h4>
<div class="abs recent" style="top:2068px">
  <div class="recent-thumb" style="background:linear-gradient(135deg,#8a6a4a,#d9b58a)" role="img" aria-label="Warm lit interior project"></div>
  <div><div class="recent-title">Lorem ipsum dolor sit amet, consectetur adipisicing elit,</div><div class="recent-date">july 7, 2014</div></div>
</div>
<div class="abs recent" style="top:2171px">
  <div class="recent-thumb" style="background:linear-gradient(135deg,#e6e6e6,#6f7478)" role="img" aria-label="Modern dining room project"></div>
  <div><div class="recent-title">Lorem ipsum dolor sit amet, consectetur adipisicing elit,</div><div class="recent-date">july 7, 2014</div></div>
</div>

<h4 class="abs foot-title" style="left:774px">Subscribe to our Newsletter</h4>
<div class="abs mail-field">Enter Your Mail Id</div>
<div class="abs btn subscribe-btn">Subscribe</div>

<div class="abs copyright">© Copyright 2014&nbsp; zintaremura.com.&nbsp; All Rights Reserved</div>

</body>
</html>
```